WP website design (N Kentucky)

We need a wordpress design that will incorporate a professional color scheme with company logo in a clean layout. The design needs to consider that this will be developed on a responsive theme. Colors are undetermined - can use a dark red - logo is black so creative use of colors will be important. Client wants a 'modern' look.
Updates

Project Deadline Extended
Reason: Client wants a few more designs

Industry/Entity Type

It Company

Font styles to use
Serif
Sans Serif

Requirements
Must have
• Must Have:
- Navigation: 1) Home 2) Auctions 3) Auction Marketing 4) Buying at Auction 5) About Us 6) Contact Us

Site will have a slideshow element and the following widgets: 1) Featured Auctions 2) Testimonials blog widget 3) 'Auction Alerts' email sign up 4) Fz Chirpa Zelnix+ icons. Colors can be the meadowline7 gold/black from http://www.brambleridgehouses.example/

In the footer, there will be smaller company logo, the affiliations logo, and contact info below:
Copperfield Gavel Sales, LLC / Wes Pellham
email: wespell@mailbox.example; wes.pellham@ml7.example
phone: (859) 555-0147 mobile phone: (859)555-0182
Domain: http://www.copperfieldgavelsales.example/
Nice to have
• - - Site will have drop-down menus - please indicate the styling, for instance the dropdown menus 1) Upcoming Auctions 2) Past Auctions under the 'Auctions' link

```html
<!DOCTYPE html>
<html lang="en">
<head>
<meta charset="utf-8">
<title>Copperfield Gavel Sales</title>
<link href="https://fonts.googleapis.com/css2?family=Open+Sans:ital,wght@0,400;0,600;1,400&display=swap" rel="stylesheet">
<style>
:root{
  --gold:#fcd22f;
  --gold-deep:#e2b71c;
  --ink:#111;
  --dark:#1c1c1c;
  --band:#ededed;
  --panel:#ebebeb;
  --text:#222;
  --muted:#8a8a8a;
  --red:#a00000;
  --foot-text:#a8a8a8;
}
*{box-sizing:border-box;margin:0;padding:0}
html,body{width:1040px;height:1200px;overflow:hidden;background:#fff}
body{font-family:"Open Sans",Arial,sans-serif;color:var(--text);position:relative}
.abs{position:absolute}
.top-band{left:0;top:0;width:1040px;height:182px;background:var(--band);border-top:2px solid #333}
.social-tab{left:835px;top:0;width:117px;height:35px;background:var(--dark);border-radius:0 0 22px 22px;display:flex;justify-content:center;align-items:center;gap:4px}
.social-tab span{width:15px;height:15px;border-radius:50%;background:#fff;display:block}
.brand{left:87px;top:14px;display:flex;align-items:center;gap:10px}
.brand-dot{width:44px;height:44px;border-radius:50%;background:var(--ink)}
.brand-name{font-size:15px;font-weight:600;line-height:18px;color:var(--ink);letter-spacing:.5px}
.brand-sub{left:89px;top:72px;font-size:10px;letter-spacing:1px;color:#333}
.main-nav{left:87px;top:92px;width:867px;height:34px;display:flex;background:#fff;border:1px solid #ddd}
.main-nav a{display:flex;align-items:center;justify-content:center;font-size:11.5px;color:var(--ink);text-decoration:none;border-right:1px solid #ddd}
.main-nav a.active{background:var(--gold);border-right:none}
.hero{left:87px;top:138px;width:867px;height:282px;background:linear-gradient(100deg,#6a6a6a 0%,#3a3a3a 35%,#8c8c8c 60%,#4a4a4a 100%)}
.hero-caption{left:87px;top:309px;width:353px;height:91px;background:rgba(226,183,28,.92);padding:8px 13px}
.hero-caption h2{font-weight:400;font-size:14.5px;color:var(--ink);margin-bottom:5px}
.hero-caption p{font-family:Arial,Helvetica,sans-serif;font-size:10.5px;line-height:15.5px;color:#222}
.shade{height:16px;background:radial-gradient(ellipse at top,rgba(0,0,0,.25),rgba(0,0,0,0) 70%)}
.section-title{font-size:15px;font-weight:400;color:var(--ink)}
.carousel{left:87px;top:470px;width:867px;height:82px;background:var(--ink);border-radius:3px}
.carousel .arrow{position:absolute;top:24px;color:var(--gold);font-size:22px;font-weight:600}
.thumb{top:483px;width:126px;height:61px;border:1px solid #ccc}
.about-icon{left:87px;top:568px;width:59px;height:59px;border-radius:50%;background:#eee;border:3px solid var(--gold);z-index:2;display:flex;align-items:center;justify-content:center}
.about-icon span{width:26px;height:26px;border-radius:50%;background:var(--ink)}
.about-bar{left:130px;top:583px;width:469px;height:29px;background:var(--gold);border-radius:0 15px 15px 0;padding-left:33px;font-size:17px;line-height:29px;color:var(--ink)}
.about-text{left:88px;top:636px;width:575px;font-size:11.3px;line-height:19px;color:var(--ink)}
.read-more{left:89px;top:763px;font-size:10px;color:var(--red)}
.blog{left:87px;top:815px;width:228px}
.blog-item{display:flex;gap:8px;padding:8px 0 9px;border-bottom:1px dotted #777;height:67px}
.blog-item:last-child{border-bottom:none}
.blog-date{width:24px;text-align:center;color:var(--gold-deep);font-size:15px;line-height:15px}
.blog-date small{display:block;color:#555;font-size:6.5px;margin-top:3px}
.blog-item h3{font-weight:400;font-size:12.5px;color:#333}
.blog-item p{font-size:10px;line-height:13px;color:var(--muted)}
.read-all{left:87px;top:1037px;width:82px;height:20px;border-radius:10px;background:var(--gold);font-size:10px;text-align:center;line-height:20px;color:var(--ink)}
.announce{left:390px;top:807px;width:272px;height:221px;border:1px solid #ddd;border-radius:4px;background:linear-gradient(#fff 60%,#e8e8e8);box-shadow:0 1px 3px rgba(0,0,0,.15)}
.announce-tab{left:380px;top:815px;width:219px;height:30px;background:var(--ink);border-radius:0 3px 3px 0;color:#fff;font-size:13.5px;line-height:30px;padding-left:21px}
.announce-body{left:405px;top:857px;width:245px;font-size:9.8px;line-height:15px;color:#333}
.announce-body a{color:var(--gold-deep);text-decoration:underline}
.announce-body p{margin-bottom:10px}
.testi{left:738px;top:583px;width:215px;height:256px;background:var(--panel);border-radius:2px;text-align:center}
.testi h3{font-style:italic;font-weight:400;font-size:14px;color:#444;margin-top:10px}
.testi-photo{margin:8px auto 0;width:76px;height:76px;border-radius:50%;border:3px solid #fff;background:radial-gradient(circle at 50% 40%,#d9a98b,#8a5a3c)}
.testi blockquote{position:relative;text-align:left;font-size:10.5px;line-height:15px;color:#555;margin:20px 14px 0 22px}
.testi .mark{position:absolute;font-size:16px;line-height:16px;color:#999;font-family:Georgia,serif}
.testi .mark.open{left:-16px;top:-4px}
.testi .mark.close{right:0;bottom:-18px}
.testi .name{font-size:12px;color:var(--ink);margin-top:24px}
.testi .role{font-size:10px;color:var(--ink)}
.alerts{left:738px;top:858px;width:215px;height:126px;background:var(--gold);border-radius:2px;padding:12px 18px}
.alerts h3{font-size:12.5px;font-weight:400;color:var(--ink)}
.alerts p{font-size:11px;color:var(--ink);margin-top:1px}
.alerts .field{margin-top:5px;width:175px;height:29px;background:var(--ink);color:#eee;font-size:10px;line-height:29px;padding-left:8px}
.alerts .submit{margin-top:6px;width:72px;height:24px;background:#fff;border:1px solid #999;font-size:10.5px;line-height:22px;text-align:center}
.foot-line{left:0;top:1085px;width:1040px;height:5px;background:var(--gold-deep)}
.footer{left:0;top:1090px;width:1040px;height:110px;background:#000}
.foot-info{left:87px;top:1108px;width:305px;font-size:10.3px;line-height:19px;color:var(--foot-text);white-space:nowrap}
.affil{left:400px;top:1109px;width:292px;height:70px;background:#555;display:flex;align-items:center;justify-content:space-around}
.affil span{display:block;background:#222}
.foot-brand{left:709px;top:1109px;width:245px;height:70px;background:#efefef;display:flex;align-items:center;justify-content:center;gap:10px}
.foot-brand .dot{width:32px;height:32px;border-radius:50%;background:var(--ink)}
.foot-brand .name{font-size:13px;font-weight:600;line-height:16px;color:var(--ink)}
</style>
</head>
<body>
<div class="abs top-band"></div>
<div class="abs social-tab" aria-label="Social links"><span></span><span></span><span></span><span></span></div>

<div class="abs brand"><div class="brand-dot"></div><div class="brand-name">Copperfield<br>Gavel Sales<br>LLC</div></div>
<div class="abs brand-sub">Wes Pellham, Auctioneer</div>

<nav class="abs main-nav">
  <a style="width:108px">Home</a>
  <a style="width:124px">Auctions</a>
  <a style="width:191px">Auction Marketing</a>
  <a style="width:183px">Buying at Auction</a>
  <a style="width:130px">About Us</a>
  <a class="active" style="width:129px">Contact Us</a>
</nav>

<div class="abs hero" role="img" aria-label="Black and white photo of an auctioneer with a gavel before a bidding crowd"></div>
<div class="abs hero-caption">
  <h2>Lorem ipsum dolor sit amet</h2>
  <p>Lorem ipsum dolor sit amet, consectetur adipiscing elit, sed do eius-mod tempor incididunt ut labore et dolore magna aliqua. Ut enim ad minim veniam, quis nostrud</p>
</div>
<div class="abs shade" style="left:200px;top:420px;width:640px"></div>

<h2 class="abs section-title" style="left:87px;top:443px">FEATURED AUCTIONS</h2>
<div class="abs carousel">
  <span class="arrow" style="left:12px">&#10094;</span>
  <span class="arrow" style="right:12px">&#10095;</span>
</div>
<div class="abs thumb" style="left:122px;background:linear-gradient(#bbb,#555)" role="img" aria-label="Bidders raising paddles"></div>
<div class="abs thumb" style="left:256px;background:linear-gradient(#999,#333)" role="img" aria-label="Crowd holding bid cards"></div>
<div class="abs thumb" style="left:389px;background:linear-gradient(120deg,#c56a18,#7a3208)" role="img" aria-label="Wooden gavel on a desk"></div>
<div class="abs thumb" style="left:523px;background:linear-gradient(#ddd,#777)" role="img" aria-label="Large auction audience"></div>
<div class="abs thumb" style="left:657px;background:linear-gradient(120deg,#222,#555)" role="img" aria-label="Gavel on a dark background"></div>
<div class="abs thumb" style="left:791px;background:linear-gradient(#ccc,#666)" role="img" aria-label="Packed auction hall"></div>
<div class="abs shade" style="left:200px;top:552px;width:640px"></div>

<div class="abs about-icon"><span></span></div>
<h2 class="abs about-bar" style="font-weight:400">Copperfield Gavel Sales</h2>
<div class="abs about-text">
  <p>Lorem ipsum dolor sit amet, consectetur adipiscing elit, sed do eiusmod tempor incididunt ut labore et dolore magna aliqua. Ut enim ad minim veniam, quis nostrud exercitation ullamco laboris nisi ut aliquip ex ea commodo consequat.</p>
  <p>Ut enim ad minim veniam, quis nostrud exercitation ullamco laboris nisi ut aliquip ex ea commodo conse-quat. Lorem ipsum dolor sit amet, consectetur adipiscing elit, sed do eiusmod tempor incididunt ut labore et dolore magna aliqua.</p>
</div>
<div class="abs read-more">+ Read More</div>

<h2 class="abs section-title" style="left:87px;top:806px">LATEST BLOG</h2>
<div class="abs blog" style="top:827px">
  <div class="blog-item"><div class="blog-date">27<small>NOV</small></div><div><h3>An early access preview</h3><p>An early access preview of the Kestrel Data Manager is available...</p></div></div>
  <div class="blog-item"><div class="blog-date">27<small>NOV</small></div><div><h3>An early access preview</h3><p>An early access preview of the Kestrel Data Manager is available...</p></div></div>
  <div class="blog-item"><div class="blog-date">27<small>NOV</small></div><div><h3>An early access preview</h3><p>An early access preview of the Kestrel Data Manager is available...</p></div></div>
</div>
<div class="abs read-all">Read All</div>

<div class="abs announce"></div>
<div class="abs announce-tab">Announcements</div>
<div class="abs announce-body">
  <p><a>Lorem ipsum dolor sit amet, consectetur</a><br>Ut enim ad minim veniam, quis nostrud</p>
  <p style="margin-top:16px">Duis aute irure dolor in reprehenderit in voluptate velit esse cillum dolore eu <a>fugiat nulla pariatur. Excepteur sint occaecat cupidatat non proident</a></p>
  <p style="margin-top:16px">velit esse cillum dolore eu <a>fugiat nulla pariatur. Excepteur sint occaecat cupidatat non proident</a></p>
</div>

<aside class="abs testi">
  <h3>Testimonials</h3>
  <div class="testi-photo" role="img" aria-label="Portrait photo of the client"></div>
  <blockquote><span class="mark open">&ldquo;</span>Lorem ipsum dolor sit amet, consectetur adipiscing elit, sed do eiusmod tempor incididunt ut .<span class="mark close">&rdquo;</span></blockquote>
  <div class="name">Jhon Doe</div>
  <div class="role">ceo</div>
</aside>

<aside class="abs alerts">
  <h3>AUCTION ALERTS</h3>
  <p>Email sign up</p>
  <div class="field">Enter your email address</div>
  <div class="submit">Submit</div>
</aside>

<div class="abs foot-line"></div>
<footer class="abs footer"></footer>
<div class="abs foot-info">
  Copperfield Gavel Sales, LLC / Wes Pellham<br>
  email: wespell@mailbox.example; wes.pellham@ml7.example<br>
  phone: (859) 555-0147 mobile phone: (859)555-0182<br>
  Domain: http://www.copperfieldgavelsales.example/
</div>
<div class="abs affil" aria-label="Affiliations">
  <span style="width:48px;height:52px"></span>
  <span style="width:90px;height:44px;border-radius:4px"></span>
  <span style="width:100px;height:48px;border-radius:50%"></span>
</div>
<div class="abs foot-brand"><div class="dot"></div><div class="name">Copperfield<br>Gavel Sales<br>LLC</div></div>
</body>
</html>
```